The Maplewick Greenhouse Garden Nursery Cards

We are looking for a professional nice business card for the Garden Center. I attached our current cards so you have the information. We do have 2 locations so that is also listed. We like the brown fade in the front, but if you have other ideas that is fine.

Also the back of the card we would like to have the ariel picture of the nursery on the card. I have that picture attached.

I also uploaded our logo files for you.

Target Market(s)

Retail

Industry/Entity Type

Retail Garden Center

Contact Information for Business Card

I have uploaded card samples.

Colors

Designer to choose colors to be used in the design.

Requirements
Must have
• Name, email, phone, cell, locations

```html
<!DOCTYPE html>
<html lang="en">
<head>
<meta charset="utf-8">
<title>The Maplewick Greenhouse – Business Cards</title>
<link href="https://fonts.googleapis.com/css2?family=Poppins:wght@300;400;500;600&display=swap" rel="stylesheet">
<style>
  :root {
    --bg: #e9e4dc;
    --brown-dark: #5e3a22;
    --brown-mid: #8a5a38;
    --brown-light: #c08a5e;
    --band: #1f1f1d;
    --gold: #c9a632;
    --cream: #f4ecc4;
    --ink: #3a2616;
    --green-dark: #0f7a34;
    --green: #1f9a45;
    --green-light: #5cc26c;
    --icon: #2b2b28;
    --pin: #c98a5a;
  }
  * { box-sizing: border-box; margin: 0; padding: 0; }
  html, body { width: 1200px; height: 780px; overflow: hidden; }
  body {
    background: var(--bg);
    font-family: "Poppins", sans-serif;
    position: relative;
  }
  .card {
    position: absolute;
    top: 235px;
    width: 540px;
    height: 310px;
    overflow: hidden;
    border-radius: 4px;
    box-shadow: 0 10px 28px rgba(0,0,0,.22);
  }
  .card-front {
    left: 40px;
    background: linear-gradient(115deg, var(--brown-dark) 0%, var(--brown-mid) 40%, var(--brown-light) 70%, var(--brown-mid) 100%);
  }
  .card-back { left: 620px; background: var(--green); }

  /* brand mark */
  .brand {
    position: absolute;
    display: flex;
    align-items: center;
    gap: 10px;
  }
  .brand-dot {
    width: 22px; height: 22px;
    border-radius: 50%;
    background: var(--cream);
    flex: none;
  }
  .brand-name {
    font-weight: 600;
    font-size: 21px;
    line-height: 1.15;
    color: var(--cream);
  }
  .card-front .brand { left: 34px; top: 105px; width: 220px; }

  /* identity */
  .identity { position: absolute; left: 290px; top: 38px; color: var(--ink); }
  .person-name { font-size: 25px; font-weight: 500; letter-spacing: .2px; }
  .person-title { font-size: 12px; font-weight: 400; margin-top: -2px; }
  .rule { width: 46px; height: 1.5px; background: var(--ink); margin: 14px 0 12px; }
  .contact-list { list-style: none; }
  .contact-list li {
    display: flex; align-items: center; gap: 8px;
    font-size: 12px; line-height: 1; margin-bottom: 7px;
  }
  .contact-icon {
    width: 17px; height: 17px; border-radius: 50%;
    background: var(--icon);
    display: flex; align-items: center; justify-content: center;
    flex: none;
  }
  .contact-icon svg { width: 10px; height: 10px; }

  /* address band */
  .info-band {
    position: absolute; left: 0; right: 0; bottom: 0; height: 74px;
    background: var(--band);
    border-top: 2px solid var(--gold);
    box-shadow: inset 0 3px 0 var(--band), inset 0 4px 0 var(--gold);
    display: flex; align-items: center;
    padding: 6px 26px 0;
    color: #f2eee6;
  }
  .location { display: flex; align-items: center; gap: 9px; font-size: 12px; line-height: 1.35; }
  .location-pin {
    width: 18px; height: 18px; border-radius: 50%;
    background: var(--pin);
    display: flex; align-items: center; justify-content: center; flex: none;
  }
  .location-pin svg { width: 10px; height: 10px; }
  .band-divider { width: 1px; height: 32px; background: #8a7a55; margin: 0 22px; }

  /* back */
  .aerial-photo {
    position: absolute; left: 0; right: 0; top: 110px; bottom: 0;
    background: linear-gradient(130deg, #8f9a8a 0%, #a7ad9f 30%, #7c9a62 55%, #b45a5a 70%, #6b9a50 100%);
  }
  .back-swoosh { position: absolute; left: 0; top: 0; width: 540px; height: 200px; }
  .card-back .brand { left: 170px; top: 58px; width: 260px; }
  .card-back .info-band { height: 52px; justify-content: flex-start; padding-left: 30px; }
  .website { font-size: 14px; font-weight: 500; letter-spacing: .3px; }
</style>
</head>
<body>

<section class="card card-front" aria-label="Business card front">
  <div class="brand">
    <span class="brand-dot"></span>
    <span class="brand-name">The Maplewick Greenhouse</span>
  </div>

  <div class="identity">
    <h1 class="person-name">Dale Hartwell</h1>
    <p class="person-title">General Manager</p>
    <div class="rule"></div>
    <ul class="contact-list">
      <li><span class="contact-icon"><svg viewBox="0 0 10 10"><path d="M2 1l2 2-1 1.2c.6 1.2 1.6 2.2 2.8 2.8L7 6l2 2-1.3 1.3C4.5 9 1 5.5.7 2.3z" fill="#fff"/></svg></span>352-555-0147</li>
      <li><span class="contact-icon"><svg viewBox="0 0 10 10"><rect x="2.5" y=".5" width="5" height="9" rx="1" fill="none" stroke="#fff"/><circle cx="5" cy="8" r=".6" fill="#fff"/></svg></span>352-555-0193</li>
      <li><span class="contact-icon"><svg viewBox="0 0 10 10"><rect x=".8" y="2" width="8.4" height="6" fill="none" stroke="#fff"/><path d="M.8 2L5 5.5 9.2 2" fill="none" stroke="#fff"/></svg></span>dale@maplewickgreenhouse.com</li>
      <li><span class="contact-icon"><svg viewBox="0 0 10 10"><circle cx="5" cy="5" r="4" fill="none" stroke="#fff"/><path d="M1 5h8M5 1c-2 2.5-2 5.5 0 8M5 1c2 2.5 2 5.5 0 8" fill="none" stroke="#fff" stroke-width=".8"/></svg></span>www.maplewickgreenhouse.com</li>
    </ul>
  </div>

  <div class="info-band">
    <div class="location">
      <span class="location-pin"><svg viewBox="0 0 10 10"><path d="M5 .5a3.2 3.2 0 0 0-3.2 3.2C1.8 6 5 9.5 5 9.5s3.2-3.5 3.2-5.8A3.2 3.2 0 0 0 5 .5z" fill="#fff"/><circle cx="5" cy="3.7" r="1.1" fill="#c98a5a"/></svg></span>
      <span>4120 Orchard Bend Road<br>Linden Hollow, FL 33500</span>
    </div>
    <div class="band-divider"></div>
    <div class="location">
      <span class="location-pin"><svg viewBox="0 0 10 10"><path d="M5 .5a3.2 3.2 0 0 0-3.2 3.2C1.8 6 5 9.5 5 9.5s3.2-3.5 3.2-5.8A3.2 3.2 0 0 0 5 .5z" fill="#fff"/><circle cx="5" cy="3.7" r="1.1" fill="#c98a5a"/></svg></span>
      <span>2870 County Road 12<br>Fernbrook, FL 33540</span>
    </div>
  </div>
</section>

<section class="card card-back" aria-label="Business card back">
  <div class="aerial-photo" role="img" aria-label="Aerial photograph of the nursery grounds with greenhouses, rows of plants and a red-roofed building"></div>
  <svg class="back-swoosh" viewBox="0 0 540 200" preserveAspectRatio="none" aria-hidden="true">
    <defs>
      <linearGradient id="swooshFill" x1="0" y1="0" x2="1" y2="1">
        <stop offset="0" stop-color="#5cc26c"/>
        <stop offset="1" stop-color="#0f7a34"/>
      </linearGradient>
    </defs>
    <path d="M0 0H540V200C420 150 260 110 0 115Z" fill="url(#swooshFill)"/>
    <path d="M0 70C200 60 380 80 540 140V200C420 150 260 110 0 115Z" fill="#1f9a45" opacity=".7"/>
  </svg>
  <div class="brand">
    <span class="brand-dot"></span>
    <span class="brand-name">The Maplewick Greenhouse</span>
  </div>
  <div class="info-band">
    <span class="website">www.maplewickgreenhouse.com</span>
  </div>
</section>

</body>
</html>
```